TRV Conference Newsletter Postcard

We need a template design for a direct mailer postcard that we are sending to potential attendees. The attached templates include the dimensions of the postcard. It is a panel/map type of postcard so it has 8 surfaces that need to have content on them. The purpose of this project is to get people to sign up and attend our conference in May. I have attached what type of layout we would like to have on each panel of the postcard.

Target Market(s)

Category Managers, Shopper Insights, Shopper Marketing

Industry/Entity Type

Consumer

Font styles to use
Sans Serif

Requirements
Must have
• A fun but clean template that includes designs, graphics, elements that show lists, our agenda, pop up graphics that can show facts and stats.
• An interesting shopper cart graphic that include insights, analytics, data, networking, etc.
Nice to have
• Maybe some fun content based on the conference title.
Should not have
• No animated characters. We want this to be clean and innovative, but fun.

```html
<!DOCTYPE html>
<html lang="en">
<head>
<meta charset="utf-8">
<title>TRV 2017 Conference Postcard</title>
<link href="https://fonts.googleapis.com/css2?family=Roboto:wght@300;400;700;900&family=Roboto+Condensed:wght@400;700&family=Open+Sans:wght@300;400;700&display=swap" rel="stylesheet">
<style>
  :root{
    --brand-blue:#1a80cc;
    --navy:#0a1a33;
    --navy-deep:#07122a;
    --glow:#2f95e0;
    --cyan:#29a9e8;
    --tab:#0d5f8f;
    --ink-light:#e8eef7;
    --name-blue:#1a7fd0;
    --red:#e0262b;
    --band-top:#2c86c4;
    --band-bottom:#0e2a46;
  }
  *{box-sizing:border-box;margin:0;padding:0}
  html,body{width:1200px;height:1200px;overflow:hidden;background:#d7d8dc}
  body{position:relative;font-family:"Roboto",sans-serif}
  .postcard{position:absolute;left:0;top:217px;width:1364px;height:870px;transform:scale(.8798);transform-origin:0 0;overflow:hidden;background:#fff}

  .header-band{position:absolute;left:0;top:0;width:1364px;height:107px;background:var(--brand-blue);color:#fff}
  .agenda-title{position:absolute;left:0;width:674px;top:34px;text-align:center;font-weight:700;font-size:32px;letter-spacing:.3px}
  .speaker-title{position:absolute;left:725px;top:32px;font-weight:700;font-size:26px;line-height:28px}
  .venue{position:absolute;right:96px;top:34px;text-align:right;font-weight:700;font-size:11px;line-height:13px}
  .venue .big{font-size:12px}
  .event-date{position:absolute;left:1278px;top:33px;border-left:1.5px solid #fff;padding-left:9px;font-weight:700;font-size:26px;line-height:22px}
  .event-date small{display:block;font-size:17px;line-height:18px}

  .agenda-panel{position:absolute;left:0;top:107px;width:682px;height:763px;
    background:radial-gradient(ellipse 330px 420px at 470px 720px,var(--glow) 0%,#17548f 35%,var(--navy) 75%,var(--navy-deep) 100%);color:var(--ink-light)}
  .day-tab{position:absolute;width:166px;height:38px;background:var(--tab);border:2px solid var(--cyan);box-shadow:4px -4px 0 var(--cyan);display:flex;font-size:12px;line-height:12px;padding:5px 7px}
  .day-tab .day{width:62px;border-right:1.5px solid #fff;white-space:nowrap}
  .day-tab.wide{width:176px}
  .day-tab.wide .day{width:74px}
  .day-tab .track{padding-left:12px}
  .day-tab b{font-weight:700;display:block}
  .timeline{position:absolute;border-left:1.5px solid #c6d3e6}
  .slot{position:absolute;left:22px;width:210px}
  .slot::before{content:"";position:absolute;left:-23px;top:8px;width:7px;height:7px;border-top:1.5px solid #c6d3e6;border-right:1.5px solid #c6d3e6;transform:rotate(45deg)}
  .slot .time{font-weight:700;font-size:13px;color:#fff;display:block;line-height:14px}
  .slot .label{font-size:12.5px;line-height:13px;font-weight:400;letter-spacing:.3px}
  .slot .note{font-size:9px;line-height:10px;display:block;padding-left:4px}
  .org-seal{position:absolute;left:607px;top:688px;width:66px;height:66px;border-radius:50%;background:#fff;border:3px solid #1a4d8a;display:flex;align-items:center;justify-content:center;color:#1a4d8a;font-weight:700;font-size:17px}

  .speaker-panel{position:absolute;left:682px;top:107px;width:682px;height:513px;background:linear-gradient(120deg,#dfe2e6 0%,#f6f7f8 40%,#e6e8eb 100%)}
  .speaker{position:absolute;width:260px;text-align:center}
  .photo{width:114px;height:114px;border-radius:50%;border:2px solid var(--name-blue);margin:0 auto 10px;background:radial-gradient(circle at 50% 40%,#b9a69a 0%,#8d7b72 45%,#d9d9d9 100%)}
  .speaker .name{font-family:"Roboto Condensed",sans-serif;font-weight:700;color:var(--name-blue);font-size:16px;line-height:16px}
  .speaker .role{font-family:"Roboto Condensed",sans-serif;color:var(--name-blue);font-size:14px;line-height:16px}
  .speaker .creds{font-family:"Roboto Condensed",sans-serif;color:#333;font-size:8.5px;line-height:10px;margin-top:3px}

  .promo-band{position:absolute;left:682px;top:620px;width:682px;height:192px;background:linear-gradient(180deg,var(--band-top) 0%,#1b5f92 50%,var(--band-bottom) 100%)}
  .stat-box{position:absolute;top:18px;width:214px;height:158px;background:#f4f5f6;font-family:"Open Sans",sans-serif;color:var(--brand-blue);text-align:center;padding-top:14px}
  .stat-box .cart{display:block;margin:0 auto}
  .stat-box .figure{font-weight:700;font-size:34px;line-height:36px;margin-top:2px}
  .stat-box .caption{font-weight:300;font-size:15px;line-height:17px;color:#1d5d93;padding:0 14px}
  .discount-badge{position:absolute;left:519px;top:-48px;width:136px;height:136px;border-radius:50%;background:#fff;border:4px solid #1b5f92;box-shadow:0 0 0 3px #fff;text-align:center;padding-top:20px}
  .discount-badge .pct{color:var(--red);font-weight:900;font-size:48px;line-height:48px;letter-spacing:-1px}
  .discount-badge .word{font-weight:700;font-size:18px;line-height:20px;color:#111}
  .discount-badge .small{font-weight:700;font-size:10px;line-height:12px;color:#111;letter-spacing:1px}
  .promo-copy{position:absolute;left:500px;top:102px;width:172px;text-align:center;color:#fff;font-family:"Open Sans",sans-serif;font-size:16px;line-height:16px}

  .sponsor-strip{position:absolute;left:682px;top:812px;width:682px;height:58px;background:#fff;display:flex;align-items:center;justify-content:space-around;padding:0 80px}
  .sponsor{display:flex;align-items:center;gap:4px;font-weight:700;font-size:9px;color:#333;letter-spacing:.5px}
  .sponsor i{display:block;width:12px;height:12px;background:#555}
  .sponsor i.round{border-radius:50%;background:#c92a3a}
</style>
</head>
<body>
<main class="postcard">
  <header class="header-band">
    <h1 class="agenda-title">2017 AGENDA AT A GLANCE</h1>
    <h2 class="speaker-title">MEET THIS YEAR'S STARTING<br>SPEAKER LINE UP!</h2>
    <div class="venue"><span class="big">GRAND MERIDIAN</span><br>LAS VEGAS<br>NV</div>
    <div class="event-date">MAY<small>2017</small></div>
  </header>

  <section class="agenda-panel" aria-label="Agenda">
    <div class="day-tab" style="left:20px;top:23px"><div class="day">Monday<b>5/15</b></div><div class="track">Main<b>Conference</b></div></div>
    <div class="timeline" style="left:40px;top:66px;height:425px">
      <div class="slot" style="top:8px"><span class="time">1:00 - 2:15 PM</span><span class="label">Speed Networking</span></div>
      <div class="slot" style="top:61px"><span class="time">2:30 - 3:00 PM</span><span class="label">Opening Welcome</span></div>
      <div class="slot" style="top:107px"><span class="time">3:00 - 3:30 PM</span><span class="label">Keynote Speaker</span></div>
      <div class="slot" style="top:159px"><span class="time">3:30 - 4:00 PM</span><span class="label">Keynote Speaker</span></div>
      <div class="slot" style="top:212px"><span class="time">4:00 - 4:20 PM</span><span class="label">Break</span></div>
      <div class="slot" style="top:265px"><span class="time">4:20 - 5:05 PM</span><span class="label">Breakout Sessions</span></div>
      <div class="slot" style="top:321px"><span class="time">5:15 - 6:15 PM</span><span class="label">Solution Provider Demos</span><span class="note">*3 rounds,15 min rotations,<br>5 min in between</span></div>
      <div class="slot" style="top:398px"><span class="time">6:15 - 7:30 PM</span><span class="label">Networking Reception<br>&amp; Hors d'ouvres</span></div>
    </div>

    <div class="day-tab" style="left:20px;top:527px"><div class="day">Tuesday<b>5/16</b></div><div class="track">Main<b>Conference</b></div></div>
    <div class="timeline" style="left:34px;top:570px;height:150px">
      <div class="slot" style="top:22px;left:28px"><span class="time">7:00 - 8:30 AM</span><span class="label">Networking Breakfast</span></div>
      <div class="slot" style="top:77px;left:28px"><span class="time">8:30 - 8:45 AM</span><span class="label">The Days Highlights</span></div>
      <div class="slot" style="top:130px;left:28px"><span class="time">8:45 - 9:30 AM</span><span class="label">Keynote Speaker</span></div>
    </div>

    <div class="day-tab" style="left:251px;top:23px"><div class="day">Tuesday<b>5/16</b></div><div class="track">Main<b>Conference</b></div></div>
    <div class="timeline" style="left:262px;top:66px;height:640px">
      <div class="slot" style="top:8px;left:30px"><span class="time">9:30 - 10:00 AM</span><span class="label">Keynote Speaker</span></div>
      <div class="slot" style="top:60px;left:30px"><span class="time">10:00 - 10:20 AM</span><span class="label">Break</span></div>
      <div class="slot" style="top:112px;left:30px"><span class="time">10:20 - 10:50 AM</span><span class="label">IP Presentations</span></div>
      <div class="slot" style="top:164px;left:30px"><span class="time">11:00 - 11:45 AM</span><span class="label">Breakout Sessions</span></div>
      <div class="slot" style="top:212px;left:30px"><span class="time">11:45 - 1:00 PM</span><span class="label">Networking Lunch</span></div>
      <div class="slot" style="top:262px;left:30px"><span class="time">1:00 - 2:35 PM</span><span class="label">Solution Provider Demos</span><span class="note">*5 Rounds, 15 min rotations,<br>&nbsp;&nbsp;5 min in between</span></div>
      <div class="slot" style="top:321px;left:30px"><span class="time">2:45 - 3:30 PM</span><span class="label">Breakout Sessions</span></div>
      <div class="slot" style="top:374px;left:30px"><span class="time">3:40 - 4:10 PM</span><span class="label">IP Presentations</span></div>
      <div class="slot" style="top:427px;left:30px"><span class="time">4:10 - 4:30 PM</span><span class="label">Break</span></div>
      <div class="slot" style="top:472px;left:30px"><span class="time">4:30 - 5:15 PM</span><span class="label">Keynote Speaker</span></div>
      <div class="slot" style="top:522px;left:30px"><span class="time">5:15 - 6:30 PM</span><span class="label">Networking Reception &amp;<br>Hors d'ouvres</span></div>
      <div class="slot" style="top:580px;left:30px"><span class="time">6:30 PM</span><span class="label">Open Dinner</span></div>
      <div class="slot" style="top:631px;left:30px"><span class="time">8:30 PM</span><span class="label">Late Night Event</span></div>
    </div>

    <div class="day-tab wide" style="left:483px;top:22px"><div class="day">Wednesday<b>5/17</b></div><div class="track">Main<b>Conference</b></div></div>
    <div class="timeline" style="left:498px;top:65px;height:490px">
      <div class="slot" style="top:8px;left:26px"><span class="time">7:30 - 9:00 AM</span><span class="label">Networking Breakfast</span></div>
      <div class="slot" style="top:61px;left:26px"><span class="time">9:00 - 9:45 AM</span><span class="label">Keynote Speaker</span></div>
      <div class="slot" style="top:113px;left:26px"><span class="time">9:45 - 10:15 AM</span><span class="label">Keynote Speaker</span></div>
      <div class="slot" style="top:166px;left:26px"><span class="time">10:15 - 10:30 AM</span><span class="label">Break</span></div>
      <div class="slot" style="top:212px;left:26px"><span class="time">10:30 - 11:00 AM</span><span class="label">IP Presentations</span></div>
      <div class="slot" style="top:265px;left:26px"><span class="time">11:10 - 11:55 AM</span><span class="label">Breakout Sessions</span></div>
      <div class="slot" style="top:318px;left:26px"><span class="time">11:55 - 1:30 PM</span><span class="label">Networking Lunch</span></div>
      <div class="slot" style="top:370px;left:26px"><span class="time">1:30 - 3:30 PM</span><span class="label">Case Study Workshops</span></div>
      <div class="slot" style="top:423px;left:26px"><span class="time">3:30 - 4:15 PM</span><span class="label">Keynote Speaker</span></div>
      <div class="slot" style="top:476px;left:26px"><span class="time">4:15 - 4:30 PM</span><span class="label">Closing Remarks</span></div>
    </div>
    <div class="org-seal">TRV</div>
  </section>

  <section class="speaker-panel" aria-label="Speaker line up">
    <svg width="682" height="513" style="position:absolute;left:0;top:0" aria-hidden="true">
      <path d="M160 0 C260 150 300 330 230 513 L330 513 C380 330 340 150 250 0Z" fill="#ffffff" opacity=".7"/>
      <path d="M420 0 C520 160 560 330 500 513 L560 513 C610 330 580 160 480 0Z" fill="#ffffff" opacity=".5"/>
    </svg>
    <div class="speaker" style="left:72px;top:56px"><div class="photo" role="img" aria-label="Speaker portrait photo"></div><div class="name">Marcus &amp; Elena Whitford</div><div class="role">Broker Associate &amp; Realtor</div><div class="creds">Graduate, Realtor Institute (GRI)<br>Certified Luxury Home Marketing Specialist (CLHMS)</div></div>
    <div class="speaker" style="left:368px;top:56px"><div class="photo" role="img" aria-label="Speaker portrait photo"></div><div class="name">Marcus &amp; Elena Whitford</div><div class="role">Broker Associate &amp; Realtor</div><div class="creds">Graduate, Realtor Institute (GRI)<br>Certified Luxury Home Marketing Specialist (CLHMS)</div></div>
    <div class="speaker" style="left:72px;top:254px"><div class="photo" role="img" aria-label="Speaker portrait photo"></div><div class="name">Marcus &amp; Elena Whitford</div><div class="role">Broker Associate &amp; Realtor</div><div class="creds">Graduate, Realtor Institute (GRI)<br>Certified Luxury Home Marketing Specialist (CLHMS)</div></div>
    <div class="speaker" style="left:368px;top:254px"><div class="photo" role="img" aria-label="Speaker portrait photo"></div><div class="name">Marcus &amp; Elena Whitford</div><div class="role">Broker Associate &amp; Realtor</div><div class="creds">Graduate, Realtor Institute (GRI)<br>Certified Luxury Home Marketing Specialist (CLHMS)</div></div>
  </section>

  <section class="promo-band" aria-label="Stats and registration offer">
    <div class="stat-box" style="left:27px">
      <svg class="cart" width="64" height="44" viewBox="0 0 64 44" aria-hidden="true">
        <path d="M2 4 H12 L20 30 H52 L58 12 H15" fill="none" stroke="#1a80cc" stroke-width="3" stroke-linejoin="round" stroke-linecap="round"/>
        <rect x="22" y="20" width="6" height="8" fill="#29a9e8"/>
        <rect x="31" y="15" width="6" height="13" fill="#29a9e8"/>
        <rect x="40" y="17" width="6" height="11" fill="#29a9e8"/>
        <circle cx="24" cy="38" r="4" fill="#1a80cc"/><circle cx="48" cy="38" r="4" fill="#1a80cc"/>
      </svg>
      <div class="figure">76%</div>
      <div class="caption">of purchase decisions are made in store</div>
    </div>
    <div class="stat-box" style="left:249px">
      <svg class="cart" width="64" height="44" viewBox="0 0 64 44" aria-hidden="true">
        <path d="M2 4 H12 L20 30 H52 L58 12 H15" fill="none" stroke="#1a80cc" stroke-width="3" stroke-linejoin="round" stroke-linecap="round"/>
        <polyline points="22,26 30,20 37,23 47,15" fill="none" stroke="#29a9e8" stroke-width="2.5" stroke-linecap="round"/>
        <circle cx="24" cy="38" r="4" fill="#1a80cc"/><circle cx="48" cy="38" r="4" fill="#1a80cc"/>
      </svg>
      <div class="figure">3 Days</div>
      <div class="caption">of insights, analytics, data &amp; networking</div>
    </div>
    <div class="discount-badge"><div class="pct">10%</div><div class="word">DISCOUNT</div><div class="small">ON<br>REGISTRATION</div></div>
    <p class="promo-copy">Register Now and Receive 10% off your conference registration</p>
  </section>

  <footer class="sponsor-strip" aria-label="Sponsors">
    <span class="sponsor"><i></i>ALDER</span>
    <span class="sponsor">NORTHVALE</span>
    <span class="sponsor"><i></i>KESTREL</span>
    <span class="sponsor"><i class="round"></i>HARBORLINE</span>
    <span class="sponsor"><i></i>ALDER</span>
    <span class="sponsor">NORTHVALE</span>
    <span class="sponsor"><i></i>KESTREL</span>
    <span class="sponsor"><i class="round"></i>PINECREST</span>
  </footer>
</main>
</body>
</html>
```